Mental Health Awareness License Plates

Below is the sample format I will need. That of a plain license plate w/o frame
*refer to image with name Licence wo Frame*
Delete Frame
Replace QR Code with “MO”
Replace 2025 sticker with “ YR
Use License Plate font (attached)
On Ribbon, keep the green background
The California front leg, needs to be gradated like a sunset and retain shape of CA
Palm trees sharpened
I need the files in a format that can be used on a website, printed or made into a poster.
One file that reads SAMPLE, one version that reads “NEWPLA8”d
The finished product should look like a license plate as shown in the example
*refer to image name finished product*
I want to clarify what we are looking for. The license plate design has been approved by the state, but we need a high res version of it in multiple file formats. The most important change we are looking for is to the ribbon. The palm trees against the sunset are fuzzy, we need those placed in front of an sunset on the front leg of the ribbon. The rear leg needs to remain green (mental health color). I hope this help clarify our design need.

```html
<!DOCTYPE html>
<html lang="en">
<head>
<meta charset="utf-8">
<title>Mental Health Awareness License Plate</title>
<link rel="stylesheet" href="https://fonts.googleapis.com/css2?family=Arimo:wght@700&family=Oswald:wght@500&display=swap">
<style>
  :root {
    --page-bg: #ffffff;
    --plate-rim: #ffffff;
    --plate-rim-edge: #9a9a9a;
    --plate-face: #bae2dc;
    --state-red: #e8414b;
    --plate-navy: #1e4a6b;
    --ribbon-top: #c9472c;
    --ribbon-mid: #e99a2f;
    --ribbon-low: #f1c24a;
    --ribbon-sea: #3fa7c4;
  }
  html, body {
    margin: 0;
    padding: 0;
    width: 1200px;
    height: 849px;
    overflow: hidden;
    background: var(--page-bg);
  }
  .canvas {
    position: relative;
    width: 1200px;
    height: 849px;
  }
  .plate {
    position: absolute;
    left: 0;
    top: 0;
  }
  .state-name {
    font-family: "Arimo", "Arial", sans-serif;
    font-weight: 700;
    fill: var(--state-red);
  }
  .plate-number {
    font-family: "Oswald", "Arial Narrow", sans-serif;
    font-weight: 500;
    fill: var(--plate-navy);
  }
  .cause-line {
    font-family: "Arimo", "Arial", sans-serif;
    font-weight: 700;
    fill: var(--plate-navy);
  }
  .rim { fill: var(--plate-rim); stroke: var(--plate-rim-edge); stroke-width: 1; }
  .face { fill: var(--plate-face); }
</style>
</head>
<body>
<div class="canvas">
  <svg class="plate" width="1200" height="849" viewBox="0 0 1200 849" xmlns="http://www.w3.org/2000/svg">
    <defs>
      <linearGradient id="ribbon-sunset" x1="0" y1="0" x2="0" y2="1">
        <stop offset="0" stop-color="var(--ribbon-top)"/>
        <stop offset="0.45" stop-color="var(--ribbon-mid)"/>
        <stop offset="0.7" stop-color="var(--ribbon-low)"/>
        <stop offset="0.85" stop-color="var(--ribbon-sea)"/>
        <stop offset="1" stop-color="var(--ribbon-mid)"/>
      </linearGradient>
    </defs>

    <rect class="rim" x="185.5" y="193.5" width="841" height="425" rx="34"/>
    <rect class="face" x="203" y="213" width="806" height="383" rx="20"/>

    <rect class="ribbon-art" role="img"
          aria-label="Awareness ribbon with palm trees in front of a sunset over the sea"
          x="229" y="306" width="140" height="248" rx="14"
          fill="url(#ribbon-sunset)"/>

    <text class="state-name" x="398" y="300" font-size="72" textLength="480" lengthAdjust="spacingAndGlyphs">California</text>

    <text class="plate-number" x="399" y="528" font-size="212" textLength="531" lengthAdjust="spacingAndGlyphs">NEWPL8</text>

    <text class="cause-line" x="418" y="573" font-size="29" textLength="397" lengthAdjust="spacingAndGlyphs">MENTAL HEALTH AWARENESS</text>
  </svg>
</div>
</body>
</html>
```